Steadfast sons flyer

Benefits of prayer
- Prayer connects you to the God of fullness. Gal. 6:8
- Prayer places you cares on the Lord. 1 Peter 5:7, Matt. 11:28
- Prayer makes you fruitful in the vineyard of the Lord-this brings honour and glory. John 15:2
- Through prayer you exercise your Kingly authority. Matt. 16:19, 18:19.
- Prayer transforms you to be like Him. Luke 9:29.
- Prayer quickens divine inheritance. Luke 5:3-6
- Prayer will stir divine potentials in you. 2 Tim. 1:6
- And many more!

Experience the might and possibilities of prayer.

Join the Steadfast Sons Ministry!

```html
<!DOCTYPE html>
<html lang="en">
<head>
<meta charset="utf-8">
<title>Steadfast sons flyer</title>
<link href="https://fonts.googleapis.com/css2?family=Dancing+Script:wght@600&family=Source+Sans+3:wght@400;600&family=Roboto+Condensed:ital,wght@1,700&display=swap" rel="stylesheet">
<style>
  :root {
    --stage: #1c1c1c;
    --glow: #ffffff;
    --sky-light: #3d6aa6;
    --sky: #16447f;
    --sky-deep: #0b2650;
    --night: #05152e;
    --ink: #ffffff;
    --badge: #2f6db0;
  }
  html, body {
    margin: 0;
    width: 1200px;
    height: 1092px;
    overflow: hidden;
    background: var(--stage);
  }
  .flyer {
    position: absolute;
    left: 232px;
    top: 73px;
    width: 726px;
    height: 939px;
    overflow: hidden;
    color: var(--ink);
    font-family: "Source Sans 3", "Myriad Pro", sans-serif;
  }
  .flyer__backdrop {
    position: absolute;
    inset: 0;
    background:
      radial-gradient(ellipse 420px 330px at 90px 20px, var(--glow) 0%, rgba(255,255,255,0.85) 35%, rgba(255,255,255,0) 100%),
      radial-gradient(ellipse 260px 520px at 520px 430px, rgba(80,110,150,0.35) 0%, rgba(80,110,150,0) 100%),
      linear-gradient(180deg, var(--sky-light) 0%, var(--sky) 30%, var(--sky-deep) 65%, var(--night) 100%);
  }
  .brand {
    position: absolute;
    left: 46px;
    top: 42px;
    display: flex;
    align-items: center;
    gap: 14px;
  }
  .brand__mark {
    width: 88px;
    height: 88px;
    border-radius: 50%;
    background: var(--badge);
  }
  .brand__name {
    font-size: 26px;
    font-weight: 600;
    color: var(--badge);
  }
  .benefits__title {
    position: absolute;
    left: 44px;
    top: 240px;
    margin: 0;
    font-family: "Dancing Script", cursive;
    font-weight: 600;
    font-size: 64px;
    line-height: 1;
  }
  .benefits__list {
    position: absolute;
    left: 44px;
    top: 340px;
    margin: 0;
    padding: 0;
    list-style: none;
    font-size: 19.5px;
    line-height: 26px;
  }
  .benefits__item {
    position: relative;
    padding-left: 26px;
    margin-bottom: 25px;
    width: 600px;
  }
  .benefits__item--dot::before {
    content: "";
    position: absolute;
    left: 1px;
    top: 6px;
    width: 14px;
    height: 14px;
    border-radius: 50%;
    background: var(--ink);
  }
  .cta {
    position: absolute;
    left: 42px;
    margin: 0;
    font-family: "Roboto Condensed", "Arial Narrow", sans-serif;
    font-style: italic;
    font-weight: 700;
    letter-spacing: -0.5px;
  }
  .cta--lead { top: 782px; font-size: 26px; }
  .cta--join { top: 832px; font-size: 37px; }
</style>
</head>
<body>
  <main class="flyer">
    <div class="flyer__backdrop" role="img" aria-label="Tall wooden cross rising into a cloudy blue sky with light breaking through at the top left"></div>

    <div class="brand">
      <span class="brand__mark"></span>
      <span class="brand__name">Rising Voices Fellowship</span>
    </div>

    <h1 class="benefits__title">Benefits of prayer</h1>

    <ul class="benefits__list">
      <li class="benefits__item benefits__item--dot">Prayer connects you to the God of fullness. Gal. 6:8</li>
      <li class="benefits__item benefits__item--dot">Prayer places you cares on the Lord. 1 Peter 5:7, Matt. 11:28</li>
      <li class="benefits__item benefits__item--dot">Prayer makes you fruitful in the vineyard of the Lord-this brings honour and glory. John 15:2</li>
      <li class="benefits__item benefits__item--dot" style="width:640px">Through prayer you exercise your Kingly authority. Matt. 16:19, 18:19.</li>
      <li class="benefits__item benefits__item--dot">Prayer transforms you to be like Him. Luke 9:29.</li>
      <li class="benefits__item benefits__item--dot">Prayer quickens divine inheritance. Luke 5:3-6</li>
      <li class="benefits__item benefits__item--dot">Prayer will stir divine potentials in you. 2 Tim. 1:6</li>
      <li class="benefits__item">And many more!</li>
    </ul>

    <p class="cta cta--lead">Experience the might and possibilities of prayer.</p>
    <p class="cta cta--join">Join the Steadfast Sons Ministry!</p>
  </main>
</body>
</html>
```